Hoopline Card Design

I have attached a zip folder that has a word document describing everyhing with what I want

Target Market(s)

College basketball coaches and media

Contact Information for Business Card

Everything I want is in the word document in the zip folder

Requirements
Must have
• Must have front back design as described in word document.
Nice to have
• I want it to look sleek and first class. It has to really stand out. I have included a few different logos, the Hoopline.com needs to be on the front and Stridewell.com needs to be on the back side with our contact info. The file I attached has an extensive word document describing everything. I would also like the front with Hoopline.com to be vertical with our twitter handles. Feel free to be creative. and even add a color background. I included PSD files

```html
<!DOCTYPE html>
<html lang="en">
<head>
<meta charset="utf-8">
<title>Hoopline Card Design</title>
<link href="https://fonts.googleapis.com/css2?family=Open+Sans:ital,wght@0,400;0,600;0,700;0,800;1,800&display=swap" rel="stylesheet">
<style>
  :root {
    --bg: #e9e6dc;
    --card: #f4f4f4;
    --yellow: #d9c21e;
    --cyan: #19aecb;
    --gray-dark: #6a6a6a;
    --gray-mid: #8a8a8a;
    --gray-text: #777;
    --navy: #2e4f8f;
    --blue: #2f8dc0;
    --gold: #d8b91b;
    --ink: #333;
  }
  * { margin: 0; padding: 0; box-sizing: border-box; }
  html, body { width: 1200px; height: 800px; overflow: hidden; }
  body {
    background: var(--bg);
    font-family: "Open Sans", Arial, sans-serif;
    position: relative;
  }
  .card {
    position: absolute;
    background: var(--card);
    box-shadow: 0 10px 24px rgba(0,0,0,.18);
    overflow: hidden;
  }

  /* Back side: landscape */
  .card-back { left: 60px; top: 200px; width: 600px; height: 343px; }
  .band { position: absolute; left: 0; width: 100%; height: 16px; display: flex; }
  .band span { flex: 1; }
  .band-top { top: 0; }
  .band-bottom { bottom: 0; }
  .band-top .a, .band-bottom .b { background: var(--yellow); }
  .band-top .b, .band-bottom .a { background: var(--cyan); }

  .brand-back {
    position: absolute; left: 36px; top: 86px;
    display: flex; align-items: center; gap: 12px;
  }
  .brand-mark { width: 58px; height: 58px; border-radius: 50%; background: var(--gray-mid); }
  .brand-name { font-size: 44px; font-weight: 800; color: var(--gray-dark); letter-spacing: -.5px; line-height: 1; }
  .tagline-back {
    position: absolute; left: 106px; top: 140px;
    font-size: 13.5px; font-weight: 800; font-style: italic; color: var(--gray-dark);
  }
  .contact {
    position: absolute; left: 356px; top: 188px; list-style: none;
    font-size: 12.5px; color: var(--gray-text);
  }
  .contact li { display: flex; align-items: center; gap: 12px; height: 25px; }
  .contact svg { width: 13px; height: 13px; fill: var(--gray-mid); flex: none; }
  .contact .name { font-weight: 700; color: var(--gray-dark); }

  /* Front side: portrait */
  .card-front { left: 760px; top: 110px; width: 340px; height: 596px; }
  .front-top {
    position: absolute; left: 0; top: 0; width: 100%; height: 290px;
    display: flex; flex-direction: column; align-items: center; justify-content: center; gap: 14px;
    text-align: center;
  }
  .brand-front { display: flex; align-items: center; gap: 10px; }
  .brand-front .dot { width: 30px; height: 30px; border-radius: 50%; background: var(--blue); }
  .brand-front .word { font-size: 40px; font-weight: 800; color: var(--gold); line-height: 1; }
  .tagline-front { font-size: 15px; font-weight: 700; color: var(--ink); line-height: 1.3; }
  .handle-main { font-size: 17px; font-weight: 700; color: var(--ink); }

  .front-bottom {
    position: absolute; left: 0; bottom: 0; width: 100%; height: 306px;
    background: linear-gradient(160deg, var(--blue) 0%, var(--navy) 100%);
    padding: 40px 40px; display: flex; flex-direction: column; gap: 30px;
  }
  .social { display: flex; align-items: flex-start; gap: 14px; color: #fff; }
  .social-mark { width: 26px; height: 26px; background: #5fb4e8; border-radius: 3px; flex: none; margin-top: 2px; }
  .social .handle { font-size: 16px; font-weight: 700; display: block; }
  .social .mail { font-size: 13.5px; opacity: .9; display: block; }
</style>
</head>
<body>

<section class="card card-back" aria-label="Stridewell.com business card, contact side">
  <div class="band band-top"><span class="a"></span><span class="b"></span></div>
  <div class="brand-back">
    <div class="brand-mark"></div>
    <div class="brand-name">Stridewell.com</div>
  </div>
  <p class="tagline-back">“The Coaches Source for Junior College Basketball Coverage”</p>
  <ul class="contact">
    <li class="name">
      <svg viewBox="0 0 16 16"><circle cx="8" cy="5" r="3.5"/><path d="M1 16c0-4 3-6 7-6s7 2 7 6z"/></svg>
      Dana Mercer
    </li>
    <li>
      <svg viewBox="0 0 16 16"><rect x="1" y="4" width="14" height="11" rx="1"/><rect x="5" y="1" width="6" height="4" fill="none" stroke="#8a8a8a" stroke-width="1.5"/></svg>
      Director/Owner
    </li>
    <li>
      <svg viewBox="0 0 16 16"><path d="M3 1l3 3-2 2c1 2 3 4 6 6l2-2 3 3-2 2C7 15 1 9 1 3z"/></svg>
      555-014-2287
    </li>
    <li>
      <svg viewBox="0 0 16 16"><rect x="1" y="3" width="14" height="10"/><path d="M1 3l7 6 7-6" fill="none" stroke="#f4f4f4" stroke-width="1.3"/></svg>
      DanaMercer@Hoopline.com
    </li>
  </ul>
  <div class="band band-bottom"><span class="a"></span><span class="b"></span></div>
</section>

<section class="card card-front" aria-label="Hoopline.com business card, front side">
  <div class="front-top">
    <div class="brand-front"><span class="dot"></span><span class="word">Hoopline.com</span></div>
    <p class="tagline-front">“Covering Junior College Basketball<br>Like NEVER Before”</p>
    <p class="handle-main">@Hoopline</p>
  </div>
  <div class="front-bottom">
    <div class="social"><span class="social-mark"></span><div><span class="handle">@DanaMercerHL</span><span class="mail">dana@hoopline.com</span></div></div>
    <div class="social"><span class="social-mark"></span><div><span class="handle">@CoachRVance</span><span class="mail">rvancehoops@mail.com</span></div></div>
    <div class="social"><span class="social-mark"></span><div><span class="handle">@CoachTLowell</span><span class="mail">coach_lowell@mail.com</span></div></div>
  </div>
</section>

</body>
</html>
```